Real Estate Entrepreneur needs a business card

I am a real estate entrepreneur, I buy houses for investment purposes, I act as a real estate agent representing buyers and sellers in residential home transactions, I am a contractor that does a wide range of home repairs and construction. I'd like a design that can stick with me through the years as my business grows and morphs to fit any niche I decide to pursue as markets change.

Target Market(s)

Anyone with interest that may be related to real estate.

Industry/Entity Type

Real Estate

Contact Information for Business Card

A card that stands out and doesn't put me in any one box. My business will evolve over time and I need a card that can stay relevant.

Colors

Designer to choose colors to be used in the design.

Requirements
Must have
• Character
Nice to have
• I'm open
Should not have
• Cliche houses and hammers

```html
<!DOCTYPE html>
<html lang="en">
<head>
<meta charset="utf-8">
<title>Reid Calder – Business Card</title>
<link rel="stylesheet" href="https://fonts.googleapis.com/css2?family=Montserrat:wght@600&family=Arimo:wght@400&display=swap">
<style>
  :root {
    --bg: #262626;
    --card: #121212;
    --card-edge: #1b1b1b;
    --ink: #f4f4f4;
    --muted: #8c8c8c;
    --silver: #9a9a9a;
    --accent: #e8262a;
  }
  * { margin: 0; padding: 0; box-sizing: border-box; }
  html, body { width: 1200px; height: 1200px; overflow: hidden; }
  body {
    background: var(--bg);
    font-family: "Arimo", Arial, sans-serif;
    position: relative;
  }
  .card {
    position: absolute;
    left: 170px;
    width: 860px;
    height: 492px;
    border-radius: 22px;
    background: var(--card);
    box-shadow: 0 18px 40px rgba(0,0,0,.45);
    overflow: hidden;
  }
  .card--back { top: 90px; background: linear-gradient(160deg, var(--card-edge), var(--card)); }
  .card--front { top: 618px; }
  .card__marble {
    position: absolute; inset: 0;
    background: radial-gradient(ellipse at 55% 45%, #1e1e1e 0%, #121212 60%, #0d0d0d 100%);
  }
  .back__name {
    position: absolute; inset: 0;
    display: flex; align-items: center; justify-content: center;
    font-family: "Montserrat", sans-serif;
    font-weight: 600;
    font-size: 54px;
    letter-spacing: 2px;
    color: var(--silver);
  }
  .front__brand {
    position: absolute; left: 58px; top: 62px;
  }
  .front__name {
    font-family: "Montserrat", sans-serif;
    font-weight: 600;
    font-size: 50px;
    letter-spacing: 1px;
    color: var(--ink);
    line-height: 1;
  }
  .front__title {
    margin-top: 8px;
    font-size: 23px;
    letter-spacing: 1.5px;
    color: var(--muted);
  }
  .contact {
    position: absolute; right: 44px; bottom: 44px;
    list-style: none;
  }
  .contact__item {
    display: flex; align-items: center; justify-content: flex-end;
    gap: 18px;
    height: 44px;
    font-size: 21px;
    color: var(--ink);
    letter-spacing: .5px;
  }
  .contact__icon { width: 36px; height: 36px; flex: none; }
</style>
</head>
<body>
  <section class="card card--back">
    <div class="back__name">REID CALDER</div>
  </section>

  <section class="card card--front">
    <div class="card__marble" role="img" aria-label="Black marble texture with fine grey veins"></div>
    <div class="front__brand">
      <div class="front__name">REID CALDER</div>
      <div class="front__title">REAL ESTATE ENTREPRENEUR</div>
    </div>
    <ul class="contact">
      <li class="contact__item">(587)555-0142
        <svg class="contact__icon" viewBox="0 0 36 36"><circle cx="18" cy="18" r="16" fill="none" stroke="var(--accent)" stroke-width="2.5"/><path d="M12 10c-1.5 1-2 3 0 7s5 7 8 8c2 .6 3.5 0 4.5-1.5l-3-3-2 1.5c-2-1-4-3-5-5l1.5-2-3-3z" fill="var(--accent)"/></svg>
      </li>
      <li class="contact__item">(403)555-0178
        <svg class="contact__icon" viewBox="0 0 36 36"><circle cx="18" cy="18" r="16" fill="none" stroke="var(--accent)" stroke-width="2.5"/><rect x="13" y="9" width="10" height="18" rx="2" fill="none" stroke="var(--accent)" stroke-width="2"/><circle cx="18" cy="24" r="1" fill="var(--accent)"/></svg>
      </li>
      <li class="contact__item">info@calderholdings.com
        <svg class="contact__icon" viewBox="0 0 36 36"><circle cx="18" cy="18" r="16" fill="none" stroke="var(--accent)" stroke-width="2.5"/><rect x="10" y="12" width="16" height="12" fill="none" stroke="var(--accent)" stroke-width="2"/><path d="M10 12l8 7 8-7" fill="none" stroke="var(--accent)" stroke-width="2"/></svg>
      </li>
      <li class="contact__item">1400, 220 9 Avenue S.W, Calgary, AB, T2P 1K3
        <svg class="contact__icon" viewBox="0 0 36 36"><circle cx="18" cy="18" r="16" fill="var(--accent)"/><path d="M18 8a6 6 0 0 0-6 6c0 5 6 12 6 12s6-7 6-12a6 6 0 0 0-6-6z" fill="var(--card)"/><circle cx="18" cy="14" r="2.2" fill="var(--accent)"/></svg>
      </li>
    </ul>
  </section>
</body>
</html>
```